We require a banner design for a 53' x 10' trailer for a future development to be displayed on the side of the highway. The development name is 712 35 Commerce Park, logo is attached. This is an industrial future development. Please also include the RWN Group logo and MIRO Development logos as well.

Industry/Entity Type

Real Estate / Construction / Developer / Industrial Future Development

Requirements
Must have
• Logos provided

```html
<!DOCTYPE html>
<html lang="en">
<head>
<meta charset="utf-8">
<title>Future of Industrial Development – 712 35 Commerce Park</title>
<link href="https://fonts.googleapis.com/css2?family=Montserrat:wght@300;500;700;800&display=swap" rel="stylesheet">
<style>
  :root {
    --peach: #fbe8df;
    --navy: #0d2640;
    --orange: #eb9a66;
    --white: #ffffff;
    --red: #e0203a;
    --sky-top: #c9a86a;
    --sky-mid: #e8b25c;
    --site-blue: #26407a;
    --site-green: #1e5e58;
  }
  * { margin: 0; padding: 0; box-sizing: border-box; }
  html, body { width: 1200px; height: 245px; overflow: hidden; background: var(--peach); }
  .banner {
    position: relative;
    width: 1200px; height: 245px;
    background: var(--peach);
    font-family: "Montserrat", sans-serif;
  }
  .panel {
    position: absolute;
    left: 19px; top: 13px;
    width: 1162px; height: 219px;
    background: var(--navy);
    overflow: hidden;
  }
  .site-photo {
    position: absolute;
    left: 548px; top: 0;
    width: 614px; height: 219px;
    background:
      linear-gradient(90deg, var(--navy) 0%, rgba(13,38,64,0) 6%),
      linear-gradient(180deg, var(--sky-top) 0%, var(--sky-mid) 38%, var(--site-green) 60%, var(--site-blue) 100%);
  }
  .headline {
    position: absolute;
    left: 61px; top: 34px;
    line-height: 1;
  }
  .headline-accent {
    display: block;
    color: var(--orange);
    font-weight: 700;
    font-size: 40px;
    letter-spacing: -0.5px;
  }
  .headline-main {
    display: block;
    color: var(--white);
    font-weight: 300;
    font-size: 39px;
    margin-top: 2px;
    letter-spacing: -0.5px;
  }
  .divider {
    position: absolute;
    left: 61px; top: 109px;
    width: 185px; height: 2px;
    background: var(--white);
  }
  .partners {
    position: absolute;
    left: 60px; top: 130px;
    height: 50px;
    display: flex;
    align-items: center;
    color: var(--white);
  }
  .partner { display: flex; align-items: center; }
  .partner-group .mark {
    width: 22px; height: 22px; border-radius: 50%;
    background: var(--red);
    margin-right: 12px;
  }
  .partner-group .name {
    font-weight: 800;
    font-size: 42px;
    letter-spacing: 1px;
  }
  .partner-park {
    margin-left: 22px;
    font-weight: 700;
    font-size: 13px;
    line-height: 1.15;
    letter-spacing: 0.5px;
  }
  .partner-dev { margin-left: 26px; }
  .partner-dev .mark {
    width: 34px; height: 34px;
    border: 2px solid var(--white);
    margin-right: 14px;
  }
  .partner-dev .name {
    font-weight: 500;
    font-size: 13px;
    line-height: 1.3;
    letter-spacing: 3px;
  }
</style>
</head>
<body>
  <div class="banner">
    <div class="panel">
      <div class="site-photo" role="img" aria-label="Photo of a large construction site at sunset with tower cranes and high-rise buildings wrapped in blue and green safety netting"></div>
      <h1 class="headline">
        <span class="headline-accent">FUTURE OF INDUSTRIAL</span>
        <span class="headline-main">DEVELOPMENT</span>
      </h1>
      <div class="divider"></div>
      <div class="partners">
        <div class="partner partner-group">
          <span class="mark"></span>
          <span class="name">RWN</span>
        </div>
        <div class="partner partner-park">712 35<br>COMMERCE<br>PARK</div>
        <div class="partner partner-dev">
          <span class="mark"></span>
          <span class="name">MIRO<br>DEVELOPMENTS</span>
        </div>
      </div>
    </div>
  </div>
</body>
</html>
```